Bright Haven Estate Sales web design

We are looking to launch an Estate Sales Website for Nashville, TN. The name of our Business is Bright Haven Estate Sales. We would like to give you a blank slate so that you can showcase your design skills for us. The few things we are looking for are a nice header graphic of a house or a stock image of an estate sale. Near the header graphic we would like a quick inquiry form. If not on the right side of the header maybe midway down the site. We potentially want to see what purple and Gold look like on the site however this is not a must. We have over 20 years of industry related experience.

1. Buttons at top of the website will be.
a. Services
b. Upcoming Sales
c. About Us
d. FAQs
e. Resources

Services we offer:
1. Estate Sales
2. Cleanouts
3. Appraisals

Sites We like:
https://www.corvellestatesales.example/

We don't have a logo yet so if you have ideas please share them with us. Below are 2 ideas however if you have your own thoughts please ignore.

1. Oval ornate frame, gold and black, with BHES in the middle, deep purple. Think of catering to high class people..font should be fancy as opposed to simple.

2. Another option, Bright Haven in bold fancy script, same colors, with Estate Sales below, small different font, black.

```html
<!DOCTYPE html>
<html lang="en">
<head>
<meta charset="utf-8">
<title>Bright Haven Estate Sales</title>
<link href="https://fonts.googleapis.com/css2?family=Poppins:wght@300;400;500;600&display=swap" rel="stylesheet">
<style>
:root{
  --purple:#7b2a8e;
  --purple-dark:#5e1f6e;
  --gold:#c8933f;
  --orange:#f0960e;
  --ink:#1e1e1e;
  --muted:#555;
  --line:#e6e1ea;
  --soft:#f6f5f8;
  --footer:#2b2b2b;
  --footer-line:#3d3d3d;
  --white:#fff;
}
*{box-sizing:border-box;margin:0;padding:0}
html,body{width:1200px;height:4106px;overflow:hidden}
body{font-family:'Poppins',sans-serif;color:var(--ink);background:var(--white);position:relative}
.abs{position:absolute}
a{color:inherit;text-decoration:none}

/* hero */
.hero{position:absolute;left:0;top:0;width:1200px;height:654px;overflow:hidden}
.hero-photo{position:absolute;inset:0;background:linear-gradient(180deg,#55636e 0%,#7d6a5a 30%,#8a5141 50%,#4f5a34 75%,#3b4a25 100%)}
.hero-shade{position:absolute;inset:0;background:linear-gradient(90deg,rgba(20,20,30,.55) 0%,rgba(20,20,30,.15) 60%,rgba(0,0,0,0) 100%)}
.topbar{position:absolute;left:0;top:0;width:1200px;height:50px;border-bottom:1px solid rgba(255,255,255,.25);background:rgba(20,22,30,.35)}
.socials{position:absolute;display:flex;gap:10px}
.socials span{width:15px;height:15px;border-radius:50%;background:var(--white);display:block}
.top-contacts{position:absolute;top:16px;right:87px;display:flex;align-items:center;gap:18px;font-size:13px;color:var(--white);white-space:nowrap}
.top-contact{display:flex;align-items:center;gap:8px}
.top-contact svg{width:17px;height:17px}
.top-sep{color:rgba(255,255,255,.7)}
.nav{position:absolute;top:70px;left:491px;display:flex;gap:33px;font-size:13px;color:var(--white);align-items:center}
.nav .cta{border:1.5px solid var(--gold);background:var(--purple);padding:6px 26px;border-radius:3px}
.hero-title{position:absolute;left:97px;top:236px;font-size:43px;font-weight:500;line-height:49px;color:var(--white);width:500px}
.btn{display:inline-flex;align-items:center;justify-content:center;background:var(--purple);color:var(--white);font-size:13px;border:1.5px solid var(--gold);border-radius:3px}
.hero-stripe{position:absolute;left:0;top:590px;width:1200px;height:64px}

/* quote form */
.quote{position:absolute;left:722px;top:158px;width:391px;height:556px;background:var(--white);box-shadow:0 8px 24px rgba(0,0,0,.14)}
.quote-head{height:89px;background:var(--purple);color:var(--gold);font-size:29px;font-weight:500;display:flex;align-items:center;justify-content:center}
.field{position:absolute;left:16px;width:352px;height:46px;border:1px solid #d8d8d8;font-size:14px;color:#9a9a9a;padding:12px 18px;background:var(--white)}
.send{position:absolute;left:23px;top:476px;width:349px;height:47px;background:var(--gold);color:var(--white);font-size:16px;display:flex;align-items:center;justify-content:center;border-radius:3px}

/* sales */
.section-title{font-size:30px;font-weight:500;color:var(--ink)}
.section-title em{font-style:normal;color:var(--purple)}
.sale-card{position:absolute;top:781px;width:245px;height:255px;border:1px solid var(--line);border-radius:3px;background:var(--white)}
.sale-img{height:171px;width:100%}
.sale-date{position:absolute;top:12px;right:10px;background:var(--orange);color:var(--ink);font-size:11px;padding:3px 12px;border-radius:10px}
.sale-name{position:absolute;left:10px;top:180px;font-size:16px;font-weight:500}
.sale-loc{position:absolute;left:10px;top:203px;font-size:12px;color:var(--purple)}

/* about */
.eyebrow{font-size:15px;color:var(--gold);text-transform:uppercase}
.body-text{font-size:12.5px;line-height:20.7px;color:#333}

/* services */
.svc-card{position:absolute;top:1852px;width:321px;height:239px;border:1px solid var(--line);background:var(--white);border-radius:3px}
.svc-icon{position:absolute;left:45px;top:-35px;width:73px;height:74px}
.svc-num{position:absolute;right:22px;top:20px;font-size:37px;font-weight:600;color:#cfcfcf}
.svc-title{position:absolute;left:35px;top:60px;font-size:19px;font-weight:500}
.svc-text{position:absolute;left:35px;top:98px;width:255px;font-size:12.5px;line-height:20.5px;color:#333}

/* why choose */
.why-title{position:absolute;left:99px;top:104px;font-size:28px;font-weight:400;line-height:35px;color:var(--white);white-space:nowrap}
.why-item{position:absolute;left:97px;display:flex;align-items:center;gap:18px;font-size:13px;line-height:20px;color:var(--white)}
.why-item i{width:42px;height:42px;border-radius:50%;background:var(--purple);display:flex;align-items:center;justify-content:center;flex:none}

/* testimonials */
.t-card{position:absolute;top:2813px;width:273px;height:251px;background:var(--white);box-shadow:0 4px 16px rgba(0,0,0,.08);border-radius:3px}
.avatar{position:absolute;left:22px;top:-19px;width:74px;height:74px;border-radius:50%;border:2px solid var(--purple);background:linear-gradient(180deg,#cfcfcf,#8d8d8d)}
.stars{position:absolute;left:20px;top:65px;color:var(--orange);font-size:25px;letter-spacing:2px}
.t-text{position:absolute;left:20px;top:108px;width:238px;font-size:12.5px;line-height:21px}
.t-rule{position:absolute;left:0;right:0;top:192px;border-top:1px solid var(--line)}
.t-name{position:absolute;left:20px;top:203px;font-size:16px}
.t-city{position:absolute;left:20px;top:224px;font-size:11px;color:#9a9a9a}

/* news */
.news-card{position:absolute;top:3343px;width:327px}
.news-img{height:191px}
.news-title{margin-top:15px;font-size:17px;font-weight:500}
.news-text{margin-top:10px;font-size:13px;line-height:20px;color:#333}
.news-card .btn{margin-top:14px;width:120px;height:33px}

/* footer */
.footer{position:absolute;left:0;top:3775px;width:1200px;height:331px;background:var(--footer);color:var(--white)}
.f-label{font-size:16px;color:var(--gold)}
.f-big{font-size:20px;display:flex;align-items:center;gap:8px;white-space:nowrap}
.f-links{position:absolute;left:571px;top:138px;font-size:13px;line-height:27px}
.f-input{position:absolute;left:856px;top:170px;width:250px;height:34px;border:1px solid #777;font-size:12px;padding:9px 16px;color:#ddd}
.f-input span{position:absolute;right:8px;top:4px;width:88px;height:24px;background:var(--gold);border-radius:2px;font-size:12px;display:flex;align-items:center;justify-content:center;color:var(--white)}
</style>
</head>
<body>

<!-- HERO -->
<header class="hero">
  <div class="hero-photo" role="img" aria-label="Red brick two-storey family house with a green lawn under a blue sky"></div>
  <div class="hero-shade"></div>
  <div class="topbar">
    <div class="socials" style="left:88px;top:17px"><span></span><span></span><span></span><span></span></div>
    <div class="top-contacts">
      <div class="top-contact">
        <svg viewBox="0 0 24 24" fill="none" stroke="#f0960e" stroke-width="2"><rect x="3" y="5" width="18" height="14" rx="2"/><path d="M3 7l9 6 9-6"/></svg>
        info@brighthaven.example
      </div>
      <span class="top-sep">/</span>
      <div class="top-contact">
        <svg viewBox="0 0 24 24" fill="none" stroke="#f0960e" stroke-width="2"><path d="M5 3h4l2 5-3 2a12 12 0 006 6l2-3 5 2v4a2 2 0 01-2 2A17 17 0 013 5a2 2 0 012-2z"/></svg>
        +1 615 555 0142
      </div>
    </div>
  </div>
  <nav class="nav">
    <a>Services</a><a>Upcoming Sales</a><a>About Us</a><a>FAQs</a><a>Resources</a>
    <a class="cta">Get in Touch</a>
  </nav>
  <h1 class="hero-title">The most trusted estate sale team in the industry.</h1>
  <a class="btn abs" style="left:104px;top:422px;width:144px;height:32px">Learn more</a>
  <svg class="hero-stripe" viewBox="0 0 1200 64" preserveAspectRatio="none">
    <polygon points="0,0 620,50 1200,0 1200,64 0,64" fill="#fff"/>
    <polygon points="0,0 620,50 620,56 0,18" fill="#f0960e"/>
    <polygon points="620,50 1200,0 1200,22 640,56" fill="#5e1f6e"/>
  </svg>
</header>

<!-- QUOTE FORM -->
<form class="quote">
  <div class="quote-head">Get Free Quote</div>
  <div class="field" style="top:118px">First name</div>
  <div class="field" style="top:182px">Last name</div>
  <div class="field" style="top:245px">Phone</div>
  <div class="field" style="top:312px">Email</div>
  <div class="field" style="top:374px;height:83px;left:19px">Message</div>
  <div class="send">Send</div>
</form>

<!-- UPCOMING SALES -->
<h2 class="section-title abs" style="left:88px;top:706px">Upcoming <em>Sales</em></h2>
<article class="sale-card" style="left:84px">
  <div class="sale-img" role="img" aria-label="Red brick colonial house" style="background:linear-gradient(180deg,#9ab7d6,#a0463a 55%,#4f7a3a)"></div>
  <span class="sale-date">5 feb 2024</span>
  <div class="sale-name">Canton Estate Sale</div><div class="sale-loc">Harlow Park, TN 37000 USA</div>
</article>
<article class="sale-card" style="left:347px">
  <div class="sale-img" role="img" aria-label="Yellow house with a porch" style="background:linear-gradient(180deg,#a9c3dc,#e6d59a 50%,#6f8f4a)"></div>
  <span class="sale-date">5 feb 2024</span>
  <div class="sale-name">Canton Estate Sale</div><div class="sale-loc">Harlow Park, TN 37000 USA</div>
</article>
<article class="sale-card" style="left:606px">
  <div class="sale-img" role="img" aria-label="Ivy-covered house with a red roof" style="background:linear-gradient(180deg,#b8cde0,#a13b2e 35%,#4d7d33)"></div>
  <span class="sale-date">5 feb 2024</span>
  <div class="sale-name">Canton Estate Sale</div><div class="sale-loc">Harlow Park, TN 37000 USA</div>
</article>
<article class="sale-card" style="left:867px">
  <div class="sale-img" role="img" aria-label="White two-storey house" style="background:linear-gradient(180deg,#8fb0d4,#e9ecef 50%,#7d8a6a)"></div>
  <span class="sale-date">5 feb 2024</span>
  <div class="sale-name">Canton Estate Sale</div><div class="sale-loc">Harlow Park, TN 37000 USA</div>
</article>

<!-- ABOUT -->
<section class="about">
  <div class="abs" style="left:0;top:1127px;width:379px;height:488px;background:var(--purple)"></div>
  <div class="abs" style="left:379px;top:1540px;width:63px;height:16px;border-right:1.5px solid var(--purple);border-bottom:1.5px solid var(--purple)"></div>
  <div class="abs" role="img" aria-label="Estate agent showing documents to a couple in a bright room" style="left:158px;top:1189px;width:338px;height:349px;border-radius:169px 169px 0 0;background:linear-gradient(180deg,#f1efec,#d9d4cf 60%,#7e746c)"></div>
  <div class="eyebrow abs" style="left:580px;top:1226px">About Us</div>
  <h2 class="abs" style="left:580px;top:1256px;font-size:30px;font-weight:500;line-height:36px">Lorem ipsum dolor sit amet<br><span style="color:var(--purple)">consectetur. Porttitor</span></h2>
  <p class="body-text abs" style="left:580px;top:1346px;width:520px">Lorem ipsum dolor sit amet consectetur. Lectus facilisis eros cras mus tempor. Orci nunc a id facilisis gravida. Duis lobortis venenatis at pulvinar maecenas quis leo. Nascetur tristique pulvinar nisl euismod a vulputate lorem bibendum ut. Sed non pretium tellus purus molestie. Tortor vitae sed eu nulla at tristique hendrerit phasellus felis. Quam vel egestas sed nibh quis mattis. Massa magna at gravida vel adipiscing consectetur. Commodo elementum.</p>
  <a class="btn abs" style="left:580px;top:1505px;width:145px;height:33px">Learn More</a>
</section>

<!-- SERVICES -->
<section class="abs" style="left:0;top:1634px;width:1200px;height:550px;background:linear-gradient(180deg,#fff,var(--soft))">
  <div class="eyebrow abs" style="left:0;width:1200px;text-align:center;top:72px">What We Do</div>
  <h2 class="section-title abs" style="left:0;width:1200px;text-align:center;top:96px;font-size:31px">We Provide <em>The Solution</em></h2>
</section>
<article class="svc-card" style="left:110px">
  <svg class="svc-icon" viewBox="0 0 73 74"><polygon points="36.5,0 73,17 73,74 0,74 0,17" fill="#7b2a8e"/><path d="M22 46l14-13 14 13M26 43v12h20V43" fill="none" stroke="#c8933f" stroke-width="2.5"/></svg>
  <div class="svc-num">01</div><div class="svc-title">Estate Sales</div>
  <p class="svc-text">Lorem ipsum dolor sit amet consectetur. Lectus facilisis eros cras mus tempor. Orci nunc a id facilisis gravida. Duis lobortis venenatis at pulvinar maecenas quis leo.</p>
</article>
<article class="svc-card" style="left:445px">
  <svg class="svc-icon" viewBox="0 0 73 74"><polygon points="36.5,0 73,17 73,74 0,74 0,17" fill="#7b2a8e"/><path d="M30 28l3 9 9 3-9 3-3 9-3-9-9-3 9-3zM47 24l2 5 5 2-5 2-2 5-2-5-5-2 5-2zM47 46l2 4 4 2-4 2-2 4-2-4-4-2 4-2z" fill="#c8933f"/></svg>
  <div class="svc-num">02</div><div class="svc-title">Cleanouts</div>
  <p class="svc-text">Lorem ipsum dolor sit amet consectetur. Lectus facilisis eros cras mus tempor. Orci nunc a id facilisis gravida. Duis lobortis venenatis at pulvinar maecenas quis leo.</p>
</article>
<article class="svc-card" style="left:779px">
  <svg class="svc-icon" viewBox="0 0 73 74"><polygon points="36.5,0 73,17 73,74 0,74 0,17" fill="#7b2a8e"/><path d="M20 56h34M24 56V46h6v10M34 56V40h6v10M44 56V34h6v22M22 40l14-10 6 4 10-9" fill="none" stroke="#c8933f" stroke-width="2.5"/></svg>
  <div class="svc-num">03</div><div class="svc-title">Appraisals</div>
  <p class="svc-text">Lorem ipsum dolor sit amet consectetur. Lectus facilisis eros cras mus tempor. Orci nunc a id facilisis gravida. Duis lobortis venenatis at pulvinar maecenas quis leo.</p>
</article>

<!-- WHY CHOOSE US -->
<section class="abs" style="left:0;top:2192px;width:1200px;height:518px;background:var(--gold);overflow:hidden">
  <div class="abs" style="left:765px;top:0;width:435px;height:518px;background:var(--purple)"></div>
  <div class="abs" style="left:1127px;top:0;width:73px;height:72px;background:var(--white)"></div>
  <div class="abs" role="img" aria-label="Smiling businessman holding a tablet in an office" style="left:622px;top:88px;width:425px;height:430px;border-radius:212px 212px 0 0;background:linear-gradient(180deg,#d9dde0,#8fa2b0 50%,#5a6d7d)"></div>
  <div class="abs" style="left:860px;top:130px;width:250px;height:250px;border:1.5px solid rgba(255,255,255,.7);border-radius:50%"></div>
  <div class="abs" style="left:588px;top:303px;width:136px;height:108px;background:var(--white);border-radius:6px;box-shadow:0 6px 18px rgba(0,0,0,.15);text-align:center">
    <svg width="40" height="40" viewBox="0 0 40 40" style="margin-top:14px"><circle cx="20" cy="20" r="19" fill="#c8933f"/><path d="M12 20l6 6 10-12" fill="none" stroke="#fff" stroke-width="3"/></svg>
    <div style="color:var(--gold);font-size:22px;letter-spacing:3px;line-height:26px">★★★</div>
  </div>
  <div class="abs" style="left:97px;top:76px;font-size:16px;color:var(--white)">Why Choose Us</div>
  <h2 class="why-title">Lorem ipsum dolor sit amet<br>consectetur. Senectus et<br>pharetra eu leo leo. At erat vel id.</h2>
  <p class="abs" style="left:104px;top:227px;width:460px;font-size:12.5px;line-height:20.5px;color:#fbf1e0">Lorem ipsum dolor sit amet consectetur. Lectus facilisis eros cras mus tempor. Orci nunc a id facilisis gravida. Duis lobortis venenatis at pulvinar maecenas quis leo.</p>
  <div class="why-item" style="top:321px"><i><svg width="22" height="22" viewBox="0 0 24 24" fill="#fff"><circle cx="12" cy="7" r="3"/><circle cx="5" cy="10" r="2.3"/><circle cx="19" cy="10" r="2.3"/><path d="M6 20a6 6 0 0112 0zM0 20a5 5 0 016-4v4zM24 20a5 5 0 00-6-4v4z"/></svg></i><span>Lorem ipsum dolor sit amet consectetur. Lectus<br>facilisis eros cras mus tempor.</span></div>
  <div class="why-item" style="top:408px"><i><svg width="22" height="22" viewBox="0 0 24 24" fill="none" stroke="#fff" stroke-width="2"><circle cx="12" cy="9" r="6"/><path d="M8 14l-2 8 6-3 6 3-2-8"/></svg></i><span>Lorem ipsum dolor sit amet consectetur. Lectus<br>facilisis eros cras mus tempor.</span></div>
</section>

<!-- TESTIMONIALS -->
<section class="abs" role="img" aria-label="Faded photo of a small house model on a desk" style="left:0;top:2710px;width:1200px;height:454px;background:linear-gradient(135deg,#f4f4f4,#e6e6e6 60%,#f1f1f1)"></section>
<div class="abs" style="left:98px;top:2815px;font-size:17px">Testimonial</div>
<h2 class="abs" style="left:98px;top:2843px;font-size:31px;font-weight:500">What They’re Saying?</h2>
<p class="abs" style="left:98px;top:2892px;width:380px;font-size:12.5px;line-height:20.5px;color:#333">Lorem ipsum dolor sit amet consectetur. Lectus facilisis eros cras mus tempor. Orci nunc a id facilisis gravida. Duis lobortis venenatis at pulvinar maecenas quis leo.</p>
<svg class="abs" style="left:100px;top:2990px" width="44" height="14" viewBox="0 0 44 14" fill="none" stroke-width="2"><path d="M16 7H3m5-5L3 7l5 5" stroke="#7b2a8e"/><path d="M28 7h13m-5-5 5 5-5 5" stroke="#333"/></svg>

<article class="t-card" style="left:494px"><div class="avatar" role="img" aria-label="Client portrait"></div><div class="stars">★★★★★</div><p class="t-text">Lorem ipsum dolor sit amet consectetur. Hac in volutpat luctus in eu. Nisi diam purus quam tortor.</p><div class="t-rule"></div><div class="t-name">Dimsgon</div><div class="t-city">New York</div></article>
<article class="t-card" style="left:791px"><div class="avatar" role="img" aria-label="Client portrait"></div><div class="stars">★★★★★</div><p class="t-text">Lorem ipsum dolor sit amet consectetur. Hac in volutpat luctus in eu. Nisi diam purus quam tortor.</p><div class="t-rule"></div><div class="t-name">Dimsgon</div><div class="t-city">New York</div></article>
<article class="t-card" style="left:1087px"><div class="avatar" role="img" aria-label="Client portrait"></div><div class="stars">★★★★★</div><p class="t-text">Lorem ipsum dolor sit amet consectetur. Hac in volutpat luctus in eu. Nisi diam purus quam tortor.</p><div class="t-rule"></div><div class="t-name">Dimsgon</div><div class="t-city">New York</div></article>

<!-- NEWS -->
<h2 class="section-title abs" style="left:0;width:1176px;text-align:center;top:3244px;line-height:35px">Find Out Latest News<br><em>and Articles</em></h2>
<article class="news-card" style="left:97px"><div class="news-img" role="img" aria-label="Row of colourful Victorian houses" style="background:linear-gradient(180deg,#eef1f3,#8d6a58 50%,#4a5a3a)"></div><div class="news-title">Lorem ipsum dolor sit amet</div><p class="news-text">Lorem ipsum dolor sit amet consectetur. Lectus facilisis eros cras mus tempor.</p><a class="btn">Read more</a></article>
<article class="news-card" style="left:442px"><div class="news-img" role="img" aria-label="New brick townhouses along a street" style="background:linear-gradient(180deg,#dfe6ec,#a58e78 45%,#b9a58a)"></div><div class="news-title">Lorem ipsum dolor sit amet</div><p class="news-text">Lorem ipsum dolor sit amet consectetur. Lectus facilisis eros cras mus tempor.</p><a class="btn">Read more</a></article>
<article class="news-card" style="left:784px"><div class="news-img" role="img" aria-label="Woman sorting items in a vintage shop" style="background:linear-gradient(180deg,#e9e0d3,#b48a5e 55%,#6e4a2e)"></div><div class="news-title">Lorem ipsum dolor sit amet</div><p class="news-text">Lorem ipsum dolor sit amet consectetur. Lectus facilisis eros cras mus tempor.</p><a class="btn">Read more</a></article>

<!-- FOOTER -->
<footer class="footer">
  <div class="f-label abs" style="left:97px;top:34px">Have Any Question?</div>
  <div class="f-big abs" style="left:97px;top:65px"><svg width="22" height="22" viewBox="0 0 24 24" fill="none" stroke="#fff" stroke-width="1.8"><path d="M5 3h4l2 5-3 2a12 12 0 006 6l2-3 5 2v4a2 2 0 01-2 2A17 17 0 013 5a2 2 0 012-2z"/></svg>+1 615 555 0142</div>
  <div class="f-label abs" style="left:856px;top:39px">Send Email</div>
  <div class="f-big abs" style="left:856px;top:65px"><svg width="18" height="18" viewBox="0 0 24 24" fill="none" stroke="#fff" stroke-width="2"><rect x="3" y="5" width="18" height="14" rx="2"/><path d="M3 7l9 6 9-6"/></svg>info@brighthaven.example</div>
  <div class="abs" style="left:0;top:119px;width:1200px;border-top:1px solid var(--footer-line)"></div>
  <p class="abs" style="left:97px;top:146px;width:320px;font-size:12px;line-height:18.5px;color:#ddd">Lorem ipsum dolor sit amet consectetur. Lectus facilisis eros cras mus tempor. Orci nunc a id facilisis gravida. Duis lobortis venenatis at pulvinar maecenas quis leo.</p>
  <div class="socials" style="left:97px;top:244px"><span></span><span></span><span></span><span></span></div>
  <div class="f-links"><div>Services</div><div>Upcoming Sales</div><div>About Us</div><div>FAQs</div><div>Resources</div></div>
  <div class="f-label abs" style="left:856px;top:139px">Newsletter</div>
  <div class="f-input">Enter your email<span>Send</span></div>
  <div class="abs" style="left:856px;top:227px;font-size:11px;color:#ccc">Copyright © 2024 All rights reserved.</div>
</footer>

</body>
</html>
```